Lirevo Nocturna

Website for a night club with live music and cabaret dancers. I would like to have the following Menu: 1.) Home; 2) The Facilities; 3) The Show; 4) Other Attractions; 5) Videos & Fotos; 6) Program; 7) Reservations; 8) Membership; 9) Contacts.

The pages should be easily editable and allow to enter text, including the menu since the final version will be in both English and Portuguese. It should have a toggle or links for the Portuguese language and the English Language.

The night club itself is called "LIREVO NOCTURNA"; and its URL is www.lirevonocturna.example.

Industry/Entity Type

Night Club

```html
<!DOCTYPE html>
<html lang="en">
<head>
<meta charset="utf-8">
<title>Lirevo Nocturna</title>
<link rel="stylesheet" href="https://fonts.googleapis.com/css2?family=Oswald:wght@300;400;500&family=Ubuntu:wght@400;500;700&display=swap">
<style>
:root{
  --plum-deep:#3a0524;
  --plum:#5c0a3c;
  --magenta:#b8128a;
  --magenta-bright:#c3108f;
  --violet:#7b1f7a;
  --gold:#f6b80d;
  --gold-light:#ffd44a;
  --orange:#f39a05;
  --ink:#1a0a18;
  --night:#170513;
  --white:#ffffff;
  --lilac:#9b4f8e;
}
*{margin:0;padding:0;box-sizing:border-box}
html,body{width:725px;height:1200px;overflow:hidden}
body{font-family:'Ubuntu',sans-serif;color:var(--white);background:var(--night);position:relative}
a{text-decoration:none;color:inherit}

.site-header{position:absolute;left:0;top:0;width:725px;height:97px;background:linear-gradient(180deg,#5a0838,var(--plum-deep))}
.brand{position:absolute;left:58px;top:14px;display:flex;align-items:center;gap:10px}
.brand-mark{width:58px;height:58px;border-radius:50%;background:var(--gold);border:3px solid #d9c7d4}
.brand-name{font-family:'Ubuntu',sans-serif;font-weight:700;font-size:24px;color:#e7d6e4;letter-spacing:.3px}
.lang-switch{position:absolute;left:528px;top:2px;height:17px;padding:0 8px;background:#2e0320;border-radius:0 0 6px 6px;font-size:7px;line-height:17px;color:#d7b5cf}
.lang-switch .active{color:var(--magenta-bright)}
.lang-switch .alt{color:var(--gold)}
.phone{position:absolute;left:517px;top:50px;display:flex;align-items:center;gap:8px}
.phone-icon{width:30px;height:30px}
.phone-number{font-family:'Oswald',sans-serif;font-size:22px;color:var(--gold)}

.main-nav{position:absolute;left:0;top:97px;width:725px;height:30px;background:linear-gradient(180deg,var(--gold-light),var(--orange));display:flex;padding-left:73px}
.main-nav a{font-family:'Oswald',sans-serif;font-weight:300;font-size:10px;color:var(--white);line-height:30px;margin-right:20px}

.hero{position:absolute;left:0;top:127px;width:725px;height:365px;background:radial-gradient(ellipse at 50% 30%,#a42a9c,#6b0f66 60%,#520a4d)}
.hero-frame{position:absolute;left:50px;top:24px;width:626px;height:302px;background:var(--white);padding:5px}
.hero-photo{width:100%;height:100%;background:linear-gradient(90deg,#2f2226 0%,#6a3e3c 22%,#a7a35a 40%,#7a4c45 55%,#a9a05c 72%,#c4bfc2 100%)}
.dots{display:flex;gap:6px}
.dot{width:10px;height:10px;border-radius:50%;background:var(--gold);border:1px solid #8a5a00}
.dot.current{background:var(--magenta-bright);border-color:#5c0a3c}
.hero .dots{position:absolute;left:327px;top:337px}

.parties{position:absolute;left:0;top:492px;width:725px;height:228px;background:linear-gradient(180deg,var(--magenta) 0%,#7a0d5c 45%,#3e0530 100%)}
.party{position:absolute;top:0;width:140px;text-align:center;padding-top:18px}
.party:nth-child(1){left:53px}
.party:nth-child(2){left:215px}
.party:nth-child(3){left:369px}
.party:nth-child(4){left:529px}
.party-photo{width:102px;height:102px;border-radius:50%;border:3px solid var(--white);margin:0 auto}
.party h3{font-size:11px;font-weight:500;margin-top:8px}
.party p{font-size:7px;line-height:10px;margin-top:5px}
.btn-learn{display:inline-block;margin-top:16px;width:56px;height:23px;border-radius:6px;background:#1e0918;font-family:'Oswald',sans-serif;font-weight:300;font-size:8px;line-height:23px;color:var(--white);text-decoration:none}

.feature{position:absolute;left:0;top:720px;width:725px;height:272px;background:var(--magenta-bright)}
.feature-photo{position:absolute;left:62px;top:19px;width:214px;height:214px;border-radius:50%;border:4px solid var(--white);background:radial-gradient(circle at 50% 45%,#b07a4a,#8a3f4e 40%,#3b1e33 75%)}
.feature-copy{position:absolute;left:308px;top:34px;width:358px}
.feature-copy h2{font-family:'Oswald',sans-serif;font-weight:400;font-size:27px;line-height:29px}
.feature-copy .sub{font-family:'Ubuntu',sans-serif;font-weight:500;font-size:18px;line-height:20px}
.feature-copy p{font-size:7.6px;line-height:10.8px;margin-top:9px}
.feature .dots{position:absolute;left:313px;top:228px}
.feature .dot{background:var(--orange);border:1px solid var(--white)}
.feature .dot.current{background:#2a0a30}

.newsletter{position:absolute;left:0;top:992px;width:725px;height:109px;background:radial-gradient(ellipse at 50% 40%,#5e2a58,#3a1534 70%);text-align:center}
.newsletter p{font-size:8.5px;margin-top:27px;letter-spacing:.2px}
.subscribe{position:absolute;left:188px;top:60px;display:flex}
.subscribe input{width:285px;height:23px;border:0;padding-left:9px;font-family:'Ubuntu',sans-serif;font-size:7px;color:#666}
.subscribe button{width:66px;height:23px;border:0;background:#e4a405;font-family:'Ubuntu',sans-serif;font-size:7.5px;color:var(--ink)}

.site-footer{position:absolute;left:0;top:1101px;width:725px;height:99px;background:var(--night)}
.footer-col{position:absolute;top:16px}
.footer-col h4{font-size:10px;font-weight:500;color:var(--lilac);letter-spacing:.3px}
.footer-col h4.name{font-family:'Oswald',sans-serif;font-weight:400;font-size:14px}
.footer-col p{font-size:7.4px;line-height:12.5px;margin-top:8px;color:var(--white)}
.footer-col address{font-style:normal;font-size:7.4px;line-height:16px;margin-top:6px;color:var(--white)}
.support{left:69px}
.location{left:284px}
.social{left:491px}
.social-links{display:flex;gap:6px;margin-top:10px}
.social-links span{width:23px;height:23px;border-radius:50%;background:var(--lilac)}
.copyright{font-size:7px;margin-top:9px;padding-left:8px}
</style>
</head>
<body>
<header class="site-header">
  <div class="brand"><span class="brand-mark"></span><span class="brand-name">Lirevo Nocturna</span></div>
  <div class="lang-switch">Select Language : <a class="active" href="#">English</a> &nbsp;|&nbsp; <a class="alt" href="#">Portuguese</a></div>
  <div class="phone">
    <svg class="phone-icon" viewBox="0 0 30 30"><circle cx="15" cy="15" r="15" fill="#b8128a"/><path d="M10 8c1-1 2 0 3 2l1 2c0 1-1 2-1 2 1 2 2 3 4 4 0 0 1-1 2-1l2 1c2 1 3 2 2 3l-1 1c-6 1-12-5-13-12z" fill="#3a0524"/></svg>
    <span class="phone-number">555 0147 2290</span>
  </div>
</header>

<nav class="main-nav">
  <a href="#">HOME</a><a href="#">THE FACILITIES</a><a href="#">THE SHOW</a><a href="#">OTHER ATTRACTIONS</a><a href="#">VIDEOS &amp; FOTOS</a><a href="#">PROGRAM</a><a href="#">RESERVATIONS</a><a href="#">MEMBERSHIP</a><a href="#">CONTACTS</a>
</nav>

<section class="hero">
  <div class="hero-frame"><div class="hero-photo" role="img" aria-label="Photo of cabaret dancers in colourful feathered carnival costumes"></div></div>
  <div class="dots"><span class="dot current"></span><span class="dot"></span><span class="dot"></span><span class="dot"></span><span class="dot"></span></div>
</section>

<section class="parties">
  <article class="party">
    <div class="party-photo" role="img" aria-label="Crowd dancing under a disco ball" style="background:radial-gradient(circle at 50% 35%,#d9a2f0,#8a3cc4 45%,#2a0d40)"></div>
    <h3>RNB PARTY</h3><p>Lorem ipsum d olor sit amet<br>esta dim aria nuno valencia</p><a class="btn-learn" href="#">LEARN MORE</a>
  </article>
  <article class="party">
    <div class="party-photo" role="img" aria-label="Party girl in a red dress" style="background:radial-gradient(circle at 45% 45%,#e8d6c4,#9a2a2a 45%,#141c33 80%)"></div>
    <h3>GIRLS PARTY</h3><p>Lorem ipsum d olor sit amet<br>esta dim aria nuno valencia</p><a class="btn-learn" href="#">LEARN MORE</a>
  </article>
  <article class="party">
    <div class="party-photo" role="img" aria-label="Cabaret performer in costume" style="background:radial-gradient(circle at 50% 50%,#b08a78,#4a342e 45%,#0d0a0c 75%)"></div>
    <h3>CABARET PARTY</h3><p>Lorem ipsum d olor sit amet<br>esta dim aria nuno valencia</p><a class="btn-learn" href="#">LEARN MORE</a>
  </article>
  <article class="party">
    <div class="party-photo" role="img" aria-label="DJ with headphones at the decks" style="background:radial-gradient(circle at 50% 40%,#e6d2c0,#8a8a90 45%,#26262c 85%)"></div>
    <h3>DJ DOLL</h3><p>Lorem ipsum d olor sit amet<br>esta dim aria nuno valencia</p><a class="btn-learn" href="#">LEARN MORE</a>
  </article>
</section>

<section class="feature">
  <div class="feature-photo" role="img" aria-label="Show poster with carnival dancers and a drummer"></div>
  <div class="feature-copy">
    <h2>DANCE UNTIL DAWN WITH</h2>
    <div class="sub">OUR COOL MUSIC</div>
    <p>Fusce euismod consequat anteorem ipsum dolor sit ametconsectetuer adipiscing elit. Pellentesque sed dolor. Aliquam congue fermentum nisl. Mauris accumsan nulla vel diam. Sed in lacus ut enim adipiscing aliquet. Nulla venenatis. In pede mi, aliquet sit amet, euismod in, auctor ut, ligula. Aliquam dapibus tincidunt metus. Praesent justo dolor, lobortis quis, lobortis dignissim, pulvinar ac, lorem. Vestibulum sed ante. Donec sagittis euismod purus.</p>
    <p>Fusce euismod consequat anteorem ipsum dolor sit ametconsectetuer adipiscing elit. Pellentesque sed dolor. Aliquam congue fermentum nisl. Mauris accumsan nulla vel diam. Sed in lacus ut enim adipiscing aliquet. Nulla venenatis. In pede mi, aliquet sit amet, euismod in, auctor ut, ligula. Aliquam dapibus tincidunt metus. Praesent justo dolor, lobortis quis, lobortis dignissim, pulvinar ac, lorem. Vestibulum sed ante. Donec sagittis euismod purus.</p>
  </div>
  <div class="dots"><span class="dot current"></span><span class="dot"></span><span class="dot"></span><span class="dot"></span></div>
</section>

<section class="newsletter">
  <p>TO GET LATEST NEWS, UPDATES AND MONTHLY, WEEKLY OFFERS SUBSCRIBE OUR NEWSLETTER</p>
  <form class="subscribe"><input type="email" placeholder="Your email id"><button type="button">SUBSCRIBE</button></form>
</section>

<footer class="site-footer">
  <div class="footer-col support">
    <h4>CUSTOMER SUPPORT</h4>
    <p>Phone: 555 0147 2290<br>Email id: info@lirevonocturna.example</p>
  </div>
  <div class="footer-col location">
    <h4 class="name">LIREVO NOCTURNA</h4>
    <address>41 HARLOW AVE STE 310,<br>MARLOW IL 60999-0117</address>
  </div>
  <div class="footer-col social">
    <h4>GET IN TOUCH WITH US</h4>
    <div class="social-links"><span></span><span></span><span></span><span></span><span></span><span></span></div>
    <p class="copyright">© 2014, ALL RIGHTS RSERVED</p>
  </div>
</footer>
</body>
</html>
```